Not another boring Business Card Design Project

This is not another boring Business Card Design Project.

We are looking for the weirdest, wackiest most boundary pushing designs that you can come up with.

If you believe that design can be fun, energetic, crazy, unpredictable, beautiful and eye-catching then read on… this project is for you.

We are Wendel Prask and we print plastic cards.

We are running a Plastic Card Design Competition.

And we need a plastic card to advertise the competition to graphic designers just like you.

The design needs to make your average designers’ jaws drop and their eyes pop out.

You can do what you wish with the card design, so long as it stands out.

We like these designs, designs that stretch the boundaries and become something beyond just another business card:

http://quorvexpixels.net/wp-content/uploads/2009/03/b48.jpg
Designer - http://www.plumtorics.com/

http://quorvexpixels.net/wp-content/uploads/2009/03/b41.jpg
Designer - http://ferrandokaltz.com/

http://images.pixelhive.com/designs/44195_732292_37774_thumbnail.jpg
Designer- Lumbro Works at Pixel Hive

http://images.pixelhive.com/designs/44195_717529_37774_thumbnail.jpg
Designer - Lumbro Works at Pixel Hive

http://quorvexpixels.net/wp-content/uploads/2009/03/b11.jpg
Designer - http://www.qv7design.com/

http://quorvexpixels.net/wp-content/uploads/2009/03/b16.jpg
Designer - http://www.wobblethistle.com/

Reason: A number of designers have said they want to submit designs and haven't yet done so, we want to give them time.

Reason: We've extended the deadline by 4 days for those who want to submit their designs over the weekend and give ourselves time to judge them

Plastic

Requirements
Nice to have
• The design needs to contain this link: zq.example/Rk7pLx and any other detail that will encourage competition entry. The design will be printed on plastic.
Should not have
• No borders (when plastic cards are punched to shape and size there is movement of 1 - 2mm, borders highlight this movement).

Keep text 3mm away from edges of the cards.

Please don't create designs to be produced on clear/transparent plastic.

```html
<!DOCTYPE html>
<html lang="en">
<head>
<meta charset="utf-8">
<title>Want to win? – Plastic Card Design Competition</title>
<link rel="stylesheet" href="https://fonts.googleapis.com/css2?family=Anton&display=swap">
<style>
  :root {
    --card-black: #000000;
    --tile-green: #8dc63f;
    --tile-blue: #00aeef;
    --tile-magenta: #ec008c;
    --tile-yellow: #fff200;
    --headline-yellow: #f4ec2c;
    --link-ink: #000000;
  }
  html, body {
    margin: 0;
    padding: 0;
    width: 785px;
    height: 1200px;
    overflow: hidden;
    background: var(--card-black);
  }
  .card {
    display: block;
    width: 785px;
    height: 1200px;
  }
  .card__background { fill: var(--card-black); }
  .tile--green { fill: var(--tile-green); }
  .tile--blue { fill: var(--tile-blue); }
  .tile--magenta { fill: var(--tile-magenta); }
  .tile--yellow { fill: var(--tile-yellow); }
  .headline,
  .entry-link {
    font-family: "Anton", "Oswald", Impact, sans-serif;
    font-weight: 400;
  }
  .headline {
    fill: var(--headline-yellow);
    font-size: 104px;
  }
  .entry-link {
    fill: var(--link-ink);
    font-size: 100px;
  }
</style>
</head>
<body>
<svg class="card" viewBox="0 0 710 1085" preserveAspectRatio="none" role="img" aria-label="Want to win? Enter at zq.example/Rk7pLx">
  <rect class="card__background" x="0" y="0" width="710" height="1085"/>

  <g class="tiles">
    <polygon class="tile tile--green" points="175,268 443,0 575,0 710,135 710,384 608,282 398,490"/>
    <polygon class="tile tile--blue" points="0,440 160,280 492,612 160,945 0,785"/>
    <polygon class="tile tile--yellow" points="177,957 500,634 710,844 710,1085 305,1085"/>
    <polygon class="tile tile--magenta" points="608,282 941,614 608,947 275,614"/>
  </g>

  <text class="headline" x="62" y="478" transform="rotate(-45 62 478)" textLength="560" lengthAdjust="spacingAndGlyphs">want to win?</text>

  <text class="entry-link" x="245" y="1030" transform="rotate(-45 245 1030)" textLength="600" lengthAdjust="spacingAndGlyphs">zq.example/Rk7pLx</text>
</svg>
</body>
</html>
```